Refresh of a rather different IT outfit website

Our web site is starting to show it's age. You can see the existing site here: www.plumbcorner.net. As a growing company we want to come across as a dynamic collection of IT experts.

We want to update the design so are open to any colour palette and look, but want to retain our current table logo. We use the logo on our business cards but with a white background - see the attached file, so you don't need to keep the brown or the green.

The design should consider the range of browsers that will be looking at the site - so please show how it will look on a wide screen laptop and a 768x1024 tablet.

We want to add some pages about our team and their skills, probably with photos of each person on the team.

This is an uncoded project - the PSD files of the design is required, not coding.
Updates

Thanks everyone for the submissions so far.  It's a holiday day in the UK today but we will get some feedback on the designs so far out to you.

Target Market(s)

Architects and other creative types looking for IT support

Industry/Entity Type

Business

Font styles to use
Serif
Sans Serif

Requirements
Must have
• Must look good on a laptop and an iPad.

```html
<!DOCTYPE html>
<html lang="en">
<head>
<meta charset="utf-8">
<title>plumbcorner – IT support for business</title>
<link href="https://fonts.googleapis.com/css2?family=Oswald:wght@400;500;600&family=Open+Sans:wght@400;600;700&display=swap" rel="stylesheet">
<style>
:root{
  --crimson:#a5123c;
  --crimson-dark:#7d0d2d;
  --ink:#333333;
  --muted:#777777;
  --rule:#e4e4e4;
  --cream:#f4eed9;
  --yellow:#f2c31b;
  --footer:#2b2b2b;
  --footer-text:#b5b5b5;
  --white:#ffffff;
}
*{box-sizing:border-box;margin:0;padding:0}
html,body{width:1200px;height:2216px;overflow:hidden}
body{font-family:"Open Sans",Arial,sans-serif;color:var(--ink);background:var(--white);font-size:13px;line-height:1.6}
.wrap{width:960px;margin:0 auto;position:relative}
h2.section-title{font-family:"Oswald",Arial,sans-serif;font-weight:500;font-size:24px;letter-spacing:1px;text-align:center;color:var(--ink);text-transform:uppercase}
.section-rule{width:60px;height:3px;background:var(--crimson);margin:10px auto 0}

/* header */
.site-header{height:70px;border-bottom:1px solid var(--rule)}
.site-header .wrap{display:flex;align-items:center;justify-content:space-between;height:70px}
.brand{display:flex;align-items:center;gap:10px;font-family:"Open Sans",Arial,sans-serif;font-weight:700;font-size:24px;color:var(--crimson)}
.brand-dot{width:14px;height:14px;background:var(--yellow);border-radius:50%}
.main-nav{display:flex;gap:2px}
.main-nav a{font-size:13px;color:var(--ink);text-decoration:none;padding:8px 11px}
.main-nav a.active{background:var(--crimson);color:var(--white)}

/* hero */
.hero{height:430px;position:relative;overflow:hidden}
.hero-photo{position:absolute;inset:0;background:linear-gradient(90deg,#dfe5ea 0%,#f2f4f6 35%,#e7ebef 55%,#fafafa 100%)}
.hero-copy{position:absolute;left:620px;top:285px;width:480px}
.hero-copy h1{font-family:"Oswald",Arial,sans-serif;font-weight:600;font-size:30px;color:var(--crimson);letter-spacing:.5px}
.hero-copy p{font-size:12px;color:var(--ink);margin-top:6px;line-height:1.5}
.hero-search{position:absolute;left:840px;top:380px;display:flex;height:30px}
.hero-search span{background:var(--yellow);color:var(--ink);font-size:12px;font-weight:600;padding:5px 10px}
.hero-search i{display:block;width:170px;background:var(--white);border:3px solid var(--yellow)}

/* services */
.services{height:600px;padding-top:70px}
.services-grid{display:grid;grid-template-columns:220px 1fr 1fr 1fr;gap:60px 40px;margin-top:50px}
.services-intro{grid-row:span 2;font-size:12px;color:var(--muted);line-height:1.8}
.service{text-align:center}
.service svg{width:34px;height:34px}
.service h3{font-family:"Open Sans",Arial,sans-serif;font-weight:700;font-size:13px;text-transform:uppercase;margin:10px 0 6px}
.service p{font-size:11.5px;color:var(--muted);line-height:1.6}

/* offer band */
.offer{height:380px;background:var(--cream)}
.offer .wrap{display:flex;align-items:center;height:380px}
.offer-text{width:330px}
.offer-text h2{font-family:"Oswald",Arial,sans-serif;font-weight:500;font-size:26px;text-transform:uppercase}
.offer-text p{font-size:15px;color:var(--ink);margin-top:12px;line-height:1.6}
.offer-art{margin-left:auto;width:560px;height:300px;border-radius:6px;background:linear-gradient(135deg,#d9e6ef 0%,#a7c2d6 55%,#f0c79a 100%)}

/* news */
.news{height:360px;padding-top:50px}
.news-grid{display:grid;grid-template-columns:repeat(3,1fr);gap:30px;margin-top:34px}
.news-card{border:1px solid var(--rule);padding:18px 20px;height:190px}
.news-date{font-size:11px;color:var(--crimson);font-weight:600}
.news-card h3{font-size:13px;font-weight:700;margin:6px 0}
.news-card p{font-size:11.5px;color:var(--muted)}

/* clients */
.clients{height:200px}
.clients-head{background:var(--cream);padding:18px 0 16px}
.clients-row{display:flex;justify-content:space-between;align-items:center;height:120px}
.client{display:flex;align-items:center;gap:8px;font-family:"Open Sans",Arial,sans-serif;font-weight:600;font-size:16px;color:#8a8a8a}
.client-mark{width:18px;height:18px;background:#bcbcbc}

/* footer */
.site-footer{height:176px;background:var(--footer);color:var(--footer-text);font-size:12px}
.footer-nav{display:flex;justify-content:center;gap:34px;padding:26px 0 20px;border-bottom:1px solid #3d3d3d}
.footer-nav a{color:var(--footer-text);text-decoration:none}
.footer-info{display:flex;justify-content:space-between;align-items:center;padding-top:22px}
.footer-contact{display:flex;gap:40px;align-items:center}
.footer-contact span{display:flex;align-items:center;gap:6px}
.footer-contact svg{width:14px;height:14px}
.social{display:flex;gap:8px}
.social i{width:26px;height:26px;border-radius:50%;background:#555}
.copyright{padding-top:16px;font-size:11px;color:#888}
</style>
</head>
<body>

<header class="site-header">
  <div class="wrap">
    <div class="brand"><span class="brand-dot"></span>plumbcorner</div>
    <nav class="main-nav">
      <a class="active" href="#">Home</a><a href="#">About</a><a href="#">What we do</a><a href="#">Team</a><a href="#">Support</a><a href="#">News blog</a><a href="#">Clients</a><a href="#">Advice</a><a href="#">Partners</a><a href="#">Contact Us</a>
    </nav>
  </div>
</header>

<section class="hero">
  <div class="hero-photo" role="img" aria-label="Photo of business people in suits in a bright office, one holding a laptop"></div>
  <div class="hero-copy">
    <h1>SERIOUS IT SUPPORT FOR BUSINESS</h1>
    <p>plumbcorner was established with a specific aim: to consistently deliver an advanced<br>IT service for ambitious growing companies across all industry sectors.</p>
  </div>
  <div class="hero-search"><span>Keywords</span><i></i></div>
</section>

<section class="services">
  <div class="wrap">
    <h2 class="section-title">What we can do for you</h2>
    <div class="section-rule"></div>
    <div class="services-grid">
      <p class="services-intro">plumbcorner offers a wide range of services tailored to meet your business needs. We aim to deliver world class support and strategic advice backed up by an effective service. We care about your business as much as you do, pairing skilled professionals with reliable systems and fast response.</p>
      <div class="service">
        <svg viewBox="0 0 34 34"><circle cx="17" cy="17" r="10" fill="none" stroke="var(--crimson)" stroke-width="4"/><circle cx="17" cy="17" r="4" fill="var(--crimson)"/></svg>
        <h3>IT Support &amp; Management</h3>
        <p>Helpdesk support, network monitoring and maintenance for your office systems and staff every day.</p>
      </div>
      <div class="service">
        <svg viewBox="0 0 34 34"><path d="M9 25h17a6 6 0 0 0 0-12 8 8 0 0 0-15-1 6.5 6.5 0 0 0-2 13z" fill="var(--crimson)"/></svg>
        <h3>Cloud Computing</h3>
        <p>Hosted email, file storage and applications that follow your team wherever they choose to work.</p>
      </div>
      <div class="service">
        <svg viewBox="0 0 34 34"><rect x="8" y="8" width="18" height="18" fill="none" stroke="var(--crimson)" stroke-width="4"/><rect x="14" y="14" width="6" height="6" fill="var(--crimson)"/></svg>
        <h3>Disaster Recovery</h3>
        <p>Backup plans and offsite copies so your data and projects come back quickly after any failure.</p>
      </div>
      <div class="service">
        <svg viewBox="0 0 34 34"><rect x="7" y="7" width="9" height="9" fill="var(--crimson)"/><rect x="18" y="7" width="9" height="9" fill="var(--crimson)"/><rect x="7" y="18" width="9" height="9" fill="var(--crimson)"/><rect x="18" y="18" width="9" height="9" fill="var(--crimson)"/></svg>
        <h3>Virtualisation</h3>
        <p>Fewer servers, lower running costs and simpler management through modern virtual platforms.</p>
      </div>
      <div class="service">
        <svg viewBox="0 0 34 34"><path d="M6 26 17 6l11 20z" fill="none" stroke="var(--crimson)" stroke-width="4" stroke-linejoin="round"/></svg>
        <h3>CAD Services</h3>
        <p>Workstations, licences and plotting set up for architects and design studios of every size.</p>
      </div>
    </div>
  </div>
</section>

<section class="offer">
  <div class="wrap">
    <div class="offer-text">
      <h2>We offer our services</h2>
      <p>plumbcorner was established with a specific aim: to consistently deliver an advanced and comprehensive IT service for ambitious growing companies across all industry sectors.</p>
    </div>
    <div class="offer-art" role="img" aria-label="Illustration of a cartoon IT consultant pointing at a tablet showing connected service icons"></div>
  </div>
</section>

<section class="news">
  <div class="wrap">
    <h2 class="section-title">Latest News/Blogs</h2>
    <div class="section-rule"></div>
    <div class="news-grid">
      <article class="news-card">
        <div class="news-date">26 April, 2014</div>
        <h3>plumbcorner mobile app now available</h3>
        <p>Log support tickets and follow their progress from your phone or tablet, with alerts sent straight to your team.</p>
      </article>
      <article class="news-card">
        <div class="news-date">26 April, 2014</div>
        <h3>New certified cloud partner status</h3>
        <p>Our engineers completed a new round of training, so we can now offer faster migration to hosted services.</p>
      </article>
      <article class="news-card">
        <div class="news-date">26 April, 2014</div>
        <h3>Five tips for a safer studio network</h3>
        <p>Simple steps every design practice can take this month to protect drawings, email and client files.</p>
      </article>
    </div>
  </div>
</section>

<section class="clients">
  <div class="clients-head"><h2 class="section-title">Our Clients/Partners</h2></div>
  <div class="wrap clients-row">
    <div class="client"><span class="client-mark"></span>Denholm Crane</div>
    <div class="client">Arvell</div>
    <div class="client"><span class="client-mark"></span>Kestrel Dale</div>
    <div class="client">Marlow Hart</div>
    <div class="client"><span class="client-mark"></span>Denholm Crane</div>
  </div>
</section>

<footer class="site-footer">
  <div class="wrap">
    <nav class="footer-nav">
      <a href="#">Home</a><a href="#">About</a><a href="#">What we do</a><a href="#">Team</a><a href="#">Support</a><a href="#">News blog</a><a href="#">Clients</a><a href="#">Advice</a><a href="#">Partners</a><a href="#">Contact Us</a>
    </nav>
    <div class="footer-info">
      <div class="footer-contact">
        <span><svg viewBox="0 0 14 14"><path d="M7 1a4 4 0 0 0-4 4c0 3 4 8 4 8s4-5 4-8a4 4 0 0 0-4-4z" fill="var(--footer-text)"/></svg>plumbcorner, 48 Ash Street, Leeds LS1 4QT</span>
        <span><svg viewBox="0 0 14 14"><path d="M3 1h3l1 3-2 1a7 7 0 0 0 4 4l1-2 3 1v3a1 1 0 0 1-1 1A11 11 0 0 1 2 2a1 1 0 0 1 1-1z" fill="var(--footer-text)"/></svg>0113 496 0725</span>
        <span>hello@plumbcorner.net</span>
      </div>
      <div class="social"><i></i><i></i><i></i><i></i><i></i></div>
    </div>
    <div class="copyright">© 2014 plumbcorner – a rather different IT outfit</div>
  </div>
</footer>

</body>
</html>
```